Startup of Management Company looking for Designers!

I am looking for an upscale website. Valmoreth will focus on Real Estate, Wealth Management, and Consulting,

Target Market(s)

investors, sellers of real estate, people looking to have their real estate management.
companies looking for consulting services

Number of Pages Required

5+ page

Font styles to use
Sans Serif

Requirements
Must have
• pictures, real.

```html
<!DOCTYPE html>
<html lang="en">
<head>
<meta charset="utf-8">
<title>Valmoreth — Real Estate, Wealth Management &amp; Consulting</title>
<link href="https://fonts.googleapis.com/css2?family=Libre+Baskerville:ital,wght@0,400;0,700;1,400&family=Oswald:wght@600&family=Rubik:ital,wght@0,400;0,500;1,400&display=swap" rel="stylesheet">
<style>
:root{
  --navy:#1d4a72;
  --navy-deep:#173c5e;
  --ink:#333a40;
  --muted:#5c6670;
  --band:#efefef;
  --white:#ffffff;
}
*{box-sizing:border-box;margin:0;padding:0}
html,body{width:1200px;height:2272px;overflow:hidden;background:var(--white)}
body{position:relative;font-family:'Rubik',sans-serif;color:var(--ink)}
.abs{position:absolute}

.topbar{left:0;top:0;width:1200px;height:75px;background:var(--navy)}
.brand{left:60px;top:22px;font-family:'Libre Baskerville',serif;font-weight:400;font-size:27px;letter-spacing:1px;color:var(--white)}
.contact-chip{top:19px;display:flex;align-items:center;gap:8px;color:var(--white)}
.contact-chip .ring{width:34px;height:34px;border:1.5px solid var(--white);border-radius:9px;display:flex;align-items:center;justify-content:center}
.contact-chip small{display:block;font-size:10.5px;line-height:13px}
.contact-chip strong{display:block;font-family:'Libre Baskerville',serif;font-weight:400;font-size:16px;line-height:20px}

.nav{left:0;top:75px;width:1200px;height:45px;background:linear-gradient(#fff 60%,#dcdcdc)}
.nav ul{list-style:none;display:flex;position:absolute;left:62px;top:0;height:45px;align-items:center}
.nav li{font-size:12px;color:#222;padding:0 20px;border-right:1px solid #e1e1e1;line-height:20px}
.nav li:last-child{border:none}
.nav li.current{color:var(--navy)}
.search{left:800px;top:83px;width:340px;height:30px;border:1px solid #d4d4d4;background:#fff;font-size:11px;color:#555;padding:8px 12px}

.hero{left:0;top:120px;width:1200px;height:630px;background:linear-gradient(100deg,#3f4a55 0%,#6e6a66 35%,#8a7e74 55%,#5b5c62 80%,#383c44 100%)}
.hero-edge{left:0;top:747px;width:1200px;height:3px;background:var(--navy)}
.headline{left:112px;top:278px;font-family:'Oswald',sans-serif;font-weight:600;font-size:56px;line-height:60px;color:var(--white);text-transform:uppercase}
.hero-sub{left:116px;top:463px;font-size:15px;color:var(--white)}
.btn{background:var(--navy);color:var(--white);font-family:'Libre Baskerville',serif;font-size:14px;letter-spacing:.3px;display:flex;align-items:center;justify-content:center}
.arrow{top:390px;width:40px;height:40px}

.card{top:668px;width:277px;height:380px;background:var(--white);box-shadow:0 2px 6px rgba(0,0,0,.12)}
.card .photo{position:absolute;left:7px;top:7px;width:263px;height:188px}
.card h3{position:absolute;left:20px;top:221px;font-family:'Libre Baskerville',serif;font-weight:700;font-size:16px;color:var(--navy)}
.card p{position:absolute;left:20px;top:250px;width:240px;font-size:12px;line-height:19.5px;color:var(--ink)}
.card .more{position:absolute;right:14px;top:346px;display:flex;gap:4px;align-items:center;font-family:'Libre Baskerville',serif;font-size:11.5px;text-decoration:underline;color:#222}

.welcome-kicker{left:204px;top:1169px;font-size:14px;color:#222}
.welcome-title{left:201px;top:1192px;font-family:'Libre Baskerville',serif;font-weight:700;font-size:33px;color:var(--navy)}
.welcome-copy{left:204px;top:1241px;width:350px;font-size:12px;line-height:21px;color:var(--muted)}
.welcome-block{left:922px;top:1286px;width:278px;height:203px;background:var(--navy)}
.welcome-photo{left:700px;top:1140px;width:346px;height:274px;border-radius:3px;background:linear-gradient(160deg,#d8d5ce,#8d8780 45%,#2b3340 80%,#1d2633)}

.testimonial{left:0;top:1489px;width:1200px;height:240px;background:var(--band)}
.quote{left:322px;top:1550px;width:600px;text-align:center;font-style:italic;font-size:13.5px;line-height:24px;color:var(--muted)}
.client{left:0;width:1200px;top:1651px;text-align:center;font-family:'Libre Baskerville',serif;font-weight:700;font-size:15px;color:#222}

.news-title{left:0;width:1200px;top:1796px;text-align:center;font-family:'Libre Baskerville',serif;font-weight:700;font-size:33px;color:var(--navy)}
.news-photo{top:1878px;width:184px;height:142px}
.news-body{top:1880px;width:260px;display:flex;flex-direction:column}
.news-date{display:flex;gap:6px;align-items:center;font-size:11.5px;color:#555;line-height:14px}
.news-head{margin-top:14px;font-family:'Libre Baskerville',serif;font-weight:700;font-size:13.5px;line-height:19px;color:var(--navy)}
.news-copy{margin-top:8px;width:245px;font-size:12px;line-height:19.5px;color:var(--muted)}

.footer{left:0;top:2096px;width:1200px;height:176px;background:var(--navy)}
.footer-brand{left:61px;top:2154px;font-family:'Libre Baskerville',serif;font-weight:400;font-size:28px;letter-spacing:1px;color:var(--white)}
.footer-note{left:61px;top:2196px;font-size:11.5px;color:#e4ebf2}
.footer-text{color:#e4ebf2;font-size:11.5px;line-height:18px}
.social{top:2163px;width:34px;height:34px;border:1.5px solid var(--white);border-radius:50%}
</style>
</head>
<body>

<header>
  <div class="abs topbar"></div>
  <div class="abs brand">VALMORETH</div>
  <div class="abs contact-chip" style="left:720px">
    <span class="ring"><svg width="18" height="18" viewBox="0 0 24 24" fill="none" stroke="#fff" stroke-width="1.8"><path d="M6.6 3.5l2.6 3.3-1.7 2.4c1.2 2.5 3 4.3 5.3 5.4l2.4-1.6 3.3 2.5-1.3 3.2c-6.4-.6-11.8-6-12.2-12.3z"/></svg></span>
    <span><small>Call Us On</small><strong>+1 555 014 2286</strong></span>
  </div>
  <div class="abs contact-chip" style="left:931px">
    <span class="ring"><svg width="18" height="14" viewBox="0 0 24 18" fill="#fff"><rect x="1" y="1" width="22" height="16" rx="3"/><path d="M3 4l9 6 9-6" stroke="#1d4a72" stroke-width="2" fill="none"/></svg></span>
    <span><small>Email Us :</small><strong>info@valmoreth.com</strong></span>
  </div>

  <nav class="abs nav">
    <ul>
      <li class="current">HOME <svg width="9" height="6" viewBox="0 0 9 6" style="margin-left:6px"><path d="M0 0h9L4.5 6z" fill="#1d4a72"/></svg></li>
      <li>ABOUT US</li><li>SERVICES</li><li>NEWS</li><li>CONTACT US</li>
    </ul>
  </nav>
  <div class="abs search">Search...</div>
  <svg class="abs" style="left:1113px;top:89px" width="20" height="20" viewBox="0 0 20 20" fill="none" stroke="#1d4a72" stroke-width="2"><circle cx="8" cy="8" r="6"/><path d="M12.5 12.5L18 18"/></svg>
</header>

<section>
  <div class="abs hero" role="img" aria-label="Photo of two smiling business colleagues at a desk"></div>
  <div class="abs hero-edge"></div>
  <h1 class="abs headline">We don’t tell<br>you to trust us<br>we earn it</h1>
  <p class="abs hero-sub">Specialize In Real Estate, Wealth Management, and Consulting</p>
  <div class="abs btn" style="left:116px;top:492px;width:147px;height:40px">CONTACT US</div>
  <svg class="abs arrow" style="left:40px" viewBox="0 0 40 40"><rect x="8" y="8" width="24" height="24" transform="rotate(45 20 20)" fill="rgba(30,40,50,.55)"/><path d="M23 13l-7 7 7 7" stroke="#fff" stroke-width="1.5" fill="none"/></svg>
  <svg class="abs arrow" style="left:1120px" viewBox="0 0 40 40"><rect x="8" y="8" width="24" height="24" transform="rotate(45 20 20)" fill="rgba(30,40,50,.55)"/><path d="M17 13l7 7-7 7" stroke="#fff" stroke-width="1.5" fill="none"/></svg>
</section>

<section>
  <article class="abs card" style="left:153px">
    <div class="photo" role="img" aria-label="Photo of house keys handed over above a contract" style="background:linear-gradient(135deg,#a9553a,#6b3b2a 50%,#2c3a50)"></div>
    <h3>Real Estate</h3>
    <p>Lorem Ipsum is simply dummy text of the printing and type setting industry been the industry It has survived typesetting only five centuries.</p>
    <span class="more">Read More <svg width="15" height="15" viewBox="0 0 16 16"><circle cx="8" cy="8" r="8" fill="#1d4a72"/><path d="M4 8h7M8 5l3 3-3 3" stroke="#fff" stroke-width="1.6" fill="none"/></svg></span>
  </article>
  <article class="abs card" style="left:461px">
    <div class="photo" role="img" aria-label="Photo of an hourglass beside stacks of coins" style="background:linear-gradient(180deg,#1e3147 0%,#2a3f55 65%,#b59b78 100%)"></div>
    <h3>Wealth Management</h3>
    <p>Lorem Ipsum is simply dummy text of the printing and type setting industry been the industry It has survived typestteing only five centuries.</p>
    <span class="more">Read More <svg width="15" height="15" viewBox="0 0 16 16"><circle cx="8" cy="8" r="8" fill="#1d4a72"/><path d="M4 8h7M8 5l3 3-3 3" stroke="#fff" stroke-width="1.6" fill="none"/></svg></span>
  </article>
  <article class="abs card" style="left:769px">
    <div class="photo" role="img" aria-label="Photo of a couple reviewing documents at a laptop" style="background:linear-gradient(160deg,#d9d6d0,#6a7f99 45%,#5a3a28 85%)"></div>
    <h3>Consulting</h3>
    <p>Lorem Ipsum is simply dummy text of the printing and type setting industry been the industry It has survived typesteeting only five centuries.</p>
    <span class="more">Read More <svg width="15" height="15" viewBox="0 0 16 16"><circle cx="8" cy="8" r="8" fill="#1d4a72"/><path d="M4 8h7M8 5l3 3-3 3" stroke="#fff" stroke-width="1.6" fill="none"/></svg></span>
  </article>
</section>

<section>
  <p class="abs welcome-kicker">WELCOME TO</p>
  <h2 class="abs welcome-title">Valmoreth</h2>
  <p class="abs welcome-copy">Lorem Ipsum is simply dummy text of the printing and type setting industry. Lorem Ipsum has been the industry stand ard dummy text ever since the 1500s, when an unknown printer took a galley of type &amp; scrambled it to make a type specimen book been the industry.</p>
  <div class="abs btn" style="left:204px;top:1361px;width:135px;height:40px">LEARN MORE</div>
  <div class="abs welcome-block"></div>
  <div class="abs welcome-photo" role="img" aria-label="Photo of a team meeting around a boardroom table"></div>
</section>

<section>
  <div class="abs testimonial"></div>
  <svg class="abs" style="left:278px;top:1548px" width="34" height="28" viewBox="0 0 34 28" fill="#1d4a72"><path d="M14 2C6 4 1 10 1 17a7 7 0 1 0 7-7c0-3 2-6 6-8zM33 2c-8 2-13 8-13 15a7 7 0 1 0 7-7c0-3 2-6 6-8z"/></svg>
  <p class="abs quote">Lorem Ipsum is simply dummy text of the printing and type setting industry. Lorem Ipsum has been the industry stand ard dummy text ever since the 1500s, when an unknown printer took a galley of type &amp; scrambled it to make a type.</p>
  <svg class="abs" style="left:786px;top:1608px" width="34" height="28" viewBox="0 0 34 28" fill="#1d4a72"><path d="M20 26c8-2 13-8 13-15a7 7 0 1 0-7 7c0 3-2 6-6 8zM1 26c8-2 13-8 13-15a7 7 0 1 0-7 7c0 3-2 6-6 8z"/></svg>
  <p class="abs client">— &nbsp;Client Name</p>
</section>

<section>
  <h2 class="abs news-title">Latest News</h2>

  <div class="abs news-photo" style="left:126px;background:linear-gradient(135deg,#1c4fa0,#5f8fd0 50%,#cfe0f4)" role="img" aria-label="Photo of a hand signing a document against glass towers"></div>
  <div class="abs news-body" style="left:333px">
    <div class="news-date"><svg width="13" height="13" viewBox="0 0 13 13" fill="none" stroke="#888"><rect x="1" y="2" width="11" height="10"/><path d="M1 5h11M4 1v2M9 1v2"/></svg>25 Feb 2021</div>
    <h3 class="news-head">Lorem Ipsum is simply dummy text of the print industry.</h3>
    <p class="news-copy">Lorem Ipsum is simply dummy text of the printing and type setting that industry as been the industry.</p>
  </div>

  <div class="abs news-photo" style="left:628px;background:linear-gradient(135deg,#c9c4bc,#8d7f72 50%,#e8e6e2)" role="img" aria-label="Photo of an agent greeting a couple"></div>
  <div class="abs news-body" style="left:835px">
    <div class="news-date"><svg width="13" height="13" viewBox="0 0 13 13" fill="none" stroke="#888"><rect x="1" y="2" width="11" height="10"/><path d="M1 5h11M4 1v2M9 1v2"/></svg>25 Feb 2021</div>
    <h3 class="news-head">Lorem Ipsum is simply dummy text of the print industry.</h3>
    <p class="news-copy">Lorem Ipsum is simply dummy text of the printing and type setting that industry as been the industry.</p>
  </div>
</section>

<footer>
  <div class="abs footer"></div>
  <div class="abs footer-brand">VALMORETH</div>
  <p class="abs footer-note">©Valmoreth - 2021 All rights reserved.</p>

  <svg class="abs" style="left:405px;top:2163px" width="22" height="28" viewBox="0 0 22 28" fill="none" stroke="#fff" stroke-width="1.5"><path d="M11 22s-7-7-7-12a7 7 0 0 1 14 0c0 5-7 12-7 12z"/><circle cx="11" cy="10" r="2.5"/><ellipse cx="11" cy="24" rx="8" ry="2.5"/></svg>
  <div class="abs footer-text" style="left:440px;top:2159px"><span style="font-size:13px;color:#fff">Valmoreth</span></div>
  <div class="abs footer-text" style="left:440px;top:2184px;width:180px">101 - Lorem ipsum simple text print type setting text.</div>

  <svg class="abs" style="left:688px;top:2161px" width="18" height="18" viewBox="0 0 24 24" fill="#fff"><path d="M6.6 2.5l3 3.8-2 2.8c1.4 2.9 3.5 5 6.2 6.3l2.8-1.9 3.9 2.9-1.5 3.8C11.5 19.4 5 13 4.5 5.5z"/></svg>
  <div class="abs footer-text" style="left:722px;top:2161px;font-size:12.5px">+1 555 014 2286</div>
  <svg class="abs" style="left:688px;top:2195px" width="18" height="14" viewBox="0 0 24 18" fill="#fff"><rect x="1" y="1" width="22" height="16" rx="2"/><path d="M2 3l10 7 10-7" stroke="#1d4a72" stroke-width="2" fill="none"/></svg>
  <div class="abs footer-text" style="left:722px;top:2194px;font-size:12px">info@valmoreth.com</div>

  <div class="abs social" style="left:918px" aria-label="Social profile link"></div>
  <div class="abs social" style="left:955px" aria-label="Social profile link"></div>
  <div class="abs social" style="left:993px" aria-label="Social profile link"></div>
</footer>

</body>
</html>
```